KVT Wellness Co Business Card for food and Beverage Falcons & Lanterns

One main business card design for a wellness enterprise which represents two brands. We need one primary card design, for two different employees. The only difference between the cards will be the name, title and phone number for each employee, all other design elements will be same.
I've uploaded the logos for each brand. I have also uploaded a mockup which I made using Google's drawing tool. I can provide example images of business cards we find attractive if you would like some help picturing what we like.
I'm picturing the color splash on the back of the card below the two logos to be a dark burgundy or blue. This may sound a bit silly but the feel of the card and color should look almost like wizard dress robes. Dark emerald green, dark blue and dark burgundy with black undertones and gold lace.
Updates

Reason: Thank you all for the submissions. I will need some extra time to give you feedback. Cheers

Target Market(s)

Healthy food and beverage industry

Industry/Entity Type

Health And Wellness

Contact Information for Business Card

On one side we would like the business name, location, title of employee, employee name and contact details. On the flip side we would like our two brand logos and a splash of color. We would like the card to have a black font with some gold accents if possible. We would also like the trim of the business card or a middle ply within the card stock to have a color other than white.

Font styles to use
Serif

Colors
ec1f27
0255a3
00a990

Requirements
Must have
• Bold dark colors, happy to provide sample photos of business cards I like from clipnook. Must have a version for two different employees. Must be sharp, modern and chic.
Nice to have
• Thick card stock layer in between the front and back of card that is either black or gold lace or something to make it feel, well let's say to make it feel expensive.
Should not have
• Should not have any cartoon-ey elements. All business.

```html
<!DOCTYPE html>
<html lang="en">
<head>
<meta charset="utf-8">
<title>KVT Wellness Co Business Card</title>
<link href="https://fonts.googleapis.com/css2?family=Montserrat:ital,wght@0,400;0,600;1,400&display=swap" rel="stylesheet">
<style>
  :root {
    --page-bg: #e9e9ea;
    --card-bg: #fbfbfa;
    --ink: #1c1c1c;
    --ink-soft: #4a4a4a;
    --band-grey: #e4e4e4;
    --accent-blue: #0b5fb0;
    --accent-burgundy: #7a1230;
    --splash-gold: #e9a52a;
    --splash-green: #1c6b34;
    --splash-burgundy: #6f1230;
    --splash-blue: #0d3d9c;
    --card-edge: #b8902f;
  }
  * { box-sizing: border-box; margin: 0; padding: 0; }
  html, body { width: 1200px; height: 863px; overflow: hidden; }
  body {
    background: var(--page-bg);
    font-family: "Montserrat", Arial, sans-serif;
    color: var(--ink);
    display: flex;
    align-items: center;
    justify-content: center;
    gap: 60px;
  }
  .card {
    position: relative;
    width: 300px;
    height: 525px;
    background: var(--card-bg);
    border-bottom: 3px solid var(--card-edge);
    border-right: 3px solid var(--card-edge);
    box-shadow: 0 10px 28px rgba(0,0,0,0.12);
    overflow: hidden;
  }
  /* front */
  .contact { position: absolute; }
  .contact-top { top: 40px; left: 40px; }
  .contact-bottom { bottom: 40px; right: 40px; text-align: right; }
  .accent-bar { position: absolute; width: 12px; height: 32px; }
  .accent-bar--blue { top: 38px; left: 16px; background: var(--accent-blue); }
  .accent-bar--burgundy { bottom: 98px; right: 0; background: var(--accent-burgundy); }
  .person-name { font-weight: 600; font-size: 15px; line-height: 1.2; }
  .person-title { font-style: italic; font-size: 11.5px; color: var(--ink-soft); margin-bottom: 14px; }
  .person-line { font-size: 11.5px; line-height: 1.55; color: var(--ink); }
  .company-band {
    position: absolute;
    top: 190px; left: 0; right: 0;
    height: 110px;
    background: var(--band-grey);
    display: flex; flex-direction: column; justify-content: center;
    padding-left: 90px;
  }
  .company-name { font-size: 17px; font-weight: 400; }
  .company-location { font-size: 12px; color: var(--ink-soft); padding-left: 10px; }
  /* back */
  .brand-name {
    position: absolute; left: 0; right: 0;
    text-align: center; font-weight: 600; font-size: 17px; color: var(--ink);
  }
  .brand-name--primary { top: 110px; }
  .brand-name--secondary { top: 235px; }
  .brand-dot {
    display: block; width: 10px; height: 10px; margin: 0 auto 10px;
    background: var(--ink); border-radius: 50%;
  }
  .color-splash {
    position: absolute; left: 0; right: 0; bottom: 0; height: 185px;
    background: linear-gradient(100deg, var(--splash-gold) 0%, var(--splash-gold) 22%, var(--splash-green) 34%, var(--splash-green) 44%, var(--splash-burgundy) 56%, var(--splash-burgundy) 74%, var(--splash-blue) 88%);
    clip-path: polygon(0 62%, 18% 52%, 32% 30%, 48% 34%, 62% 22%, 78% 18%, 88% 6%, 100% 0, 100% 100%, 0 100%);
  }
</style>
</head>
<body>
  <article class="card card--front">
    <span class="accent-bar accent-bar--blue"></span>
    <div class="contact contact-top">
      <p class="person-name">Elias Marren</p>
      <p class="person-title">Beverage Alchemist</p>
      <p class="person-line">415.555.0142</p>
      <p class="person-line">kvtwellnessco@mailbox.com</p>
    </div>
    <div class="company-band">
      <p class="company-name">KVT Wellness Co</p>
      <p class="company-location">Harrow Glen, CA</p>
    </div>
    <span class="accent-bar accent-bar--burgundy"></span>
    <div class="contact contact-bottom">
      <p class="person-name">Tobias Wrenfield</p>
      <p class="person-title">Cookie Wizard</p>
      <p class="person-line">510.555.0187</p>
      <p class="person-line">kvtwellnessco@mailbox.com</p>
    </div>
  </article>

  <article class="card card--back">
    <p class="brand-name brand-name--primary"><span class="brand-dot"></span>Falcons &amp; Lanterns</p>
    <p class="brand-name brand-name--secondary"><span class="brand-dot"></span>Lantern Gate</p>
    <div class="color-splash" role="img" aria-label="Paint splash in gold, emerald green, burgundy and deep blue"></div>
  </article>
</body>
</html>
```